VALMIKE GROUP

This is a company that provides executive protection. Our motto is "New Era in Protection"... I don't want this to look like other security websites. I want it to be clean and sharp and represent a new era. We are based in the bay area so maybe a picture of San Francisco in the background?
I want it to be able to funnel down a couple different categories.
1. About Us
2. Services (Executive Protection, Covert Protection, Residential Protection & Intelligence)
3. Iron Finch (Training & Consulting)
4. Contact Us
I want it to be very clean and modern. I don't want there to be any pictures of bodyguards with ear pieces like every other website.
Target Market(s)
Ultra High Net Worth Individuals
Coding
Coded - Design and coding required
Number of Pages Required
1 page
Requirements
Must have
- Colors of my Symbol
Nice to have
- City in the background, San Francisco, New York or the Pinehallow Club in Montana.
Should not have
- Should not look like an KVM website or have photos of bodyguards. I want this to be a clean and simple website with my logo

```html
<!DOCTYPE html>
<html lang="en">
<head>
<meta charset="utf-8">
<title>VALMIKE GROUP — New Era in Protection</title>
<link rel="stylesheet" href="https://fonts.googleapis.com/css2?family=Audiowide&family=Oswald:wght@400;500;600&family=Mulish:wght@400;700&display=swap">
<style>
:root{
  --red:#8b1519;
  --red-deep:#5f0c10;
  --ink:#2a2a2a;
  --ink-dark:#1d1d1d;
  --white:#ffffff;
  --frame:#e3e3e3;
  --frame-inner:#f7f7f7;
  --footer-line:rgba(255,255,255,.28);
}
*{margin:0;padding:0;box-sizing:border-box}
html,body{width:686px;height:1200px;overflow:hidden;background:var(--white)}
body{position:relative;font-family:"Mulish",sans-serif;color:var(--ink)}
.abs{position:absolute}
.display{font-family:"Audiowide",sans-serif}

/* top bar */
.topbar{left:0;top:0;width:686px;height:19px;background:var(--red);color:var(--white);font-size:8px}
.topbar .social{left:97px;top:5px;display:flex;gap:12px}
.dot{width:8px;height:8px;border-radius:50%;background:var(--white);display:block}
.topbar .contact{right:94px;top:4px;display:flex;gap:22px;align-items:center}
.topbar .contact span{display:flex;align-items:center;gap:5px}

.scene{left:0;top:0}

/* brand */
.brand{display:flex;align-items:center;gap:7px}
.brand-mark{width:30px;height:30px;background:var(--red)}
.brand-name{font-family:"Audiowide",sans-serif;font-size:15px;line-height:15px;letter-spacing:.5px}
.header-brand{left:92px;top:29px}
.header-brand .brand-name{color:var(--ink)}
.nav{top:38px;left:299px;font-size:10px;font-weight:700;color:var(--ink-dark)}
.nav a{color:inherit;text-decoration:none;position:absolute;white-space:nowrap}
.nav .active::after{content:"";position:absolute;left:0;right:0;bottom:-6px;height:2px;background:var(--red)}

/* hero */
.hero-title{left:0;width:686px;top:216px;text-align:center;color:var(--white);font-size:24px;letter-spacing:.5px}
.cta{left:285px;top:258px;display:flex;align-items:center}
.cta-square{width:24px;height:24px;background:var(--white);margin-right:-4px;position:relative;z-index:1}
.cta-label{background:var(--red);color:var(--white);font-family:"Oswald",sans-serif;font-weight:600;font-size:15px;letter-spacing:1.5px;padding:3px 10px 3px 20px;height:28px;line-height:22px}

/* services */
.services-eyebrow{left:0;width:686px;top:418px;text-align:center;color:var(--red);font-size:14px}
.services-title{left:0;width:686px;top:436px;text-align:center;color:var(--ink);font-size:27px}
.service{width:140px;text-align:center}
.service-icon{display:block;width:78px;height:86px;margin:0 auto}
.service-name{font-family:"Oswald",sans-serif;font-size:13px;line-height:15px;color:#1a1a1a;margin-top:5px;text-transform:uppercase}

/* about */
.about-eyebrow{left:323px;top:776px;color:var(--white);font-size:14px}
.about-title{left:323px;top:792px;color:var(--white);display:flex;align-items:baseline;gap:6px}
.about-title .big{font-size:26px}
.about-title .small{font-size:12px;letter-spacing:6px}
.about-lead{left:323px;top:828px;width:280px;color:var(--white);font-weight:700;font-size:8.6px;line-height:15.5px}
.about-body{left:323px;top:864px;width:274px;color:#e8e8e8;font-size:7.6px;line-height:14px}
.read-more{left:323px;top:944px;display:flex;align-items:center}
.read-more .sq{width:20px;height:21px;background:var(--red);margin-right:-3px;position:relative;z-index:1}
.read-more .label{background:var(--white);color:#1a1a1a;font-family:"Oswald",sans-serif;font-weight:600;font-size:10px;letter-spacing:1px;height:21px;line-height:21px;padding:0 9px 0 14px}
.about-emblem{left:92px;top:777px;width:201px;height:213px;background:rgba(214,70,76,.42);display:flex;align-items:center;justify-content:center}
.about-emblem span{font-family:"Audiowide",sans-serif;color:rgba(255,255,255,.28);font-size:26px}

/* footer */
.footer{left:0;top:1030px;width:686px;height:149px;background:var(--red);color:var(--white)}
.footer-brand{left:92px;top:33px}
.footer-brand .brand-mark{background:var(--white)}
.footer-brand .brand-name{color:var(--white)}
.footer-contact{top:41px;display:flex;align-items:center;gap:8px;font-size:9px}
.footer-icon{width:19px;height:21px;background:var(--red-deep);display:flex;align-items:center;justify-content:center}
.footer-divider{left:457px;top:42px;width:1px;height:16px;background:var(--footer-line)}
.footer-nav{left:92px;top:90px;width:502px;height:25px;border-top:1px solid var(--footer-line);border-bottom:1px solid var(--footer-line);font-size:8.6px}
.footer-nav .item{position:absolute;top:7px;transform:translateX(-50%);white-space:nowrap}
.footer-nav .sep{position:absolute;top:5px;width:1px;height:14px;background:var(--footer-line)}
.copyright{left:0;top:1179px;width:686px;height:21px;background:var(--red-deep);color:#f0f0f0;font-size:7.6px}
.copyright .left{left:93px;top:5px}
.copyright .right{right:92px;top:5px}
</style>
</head>
<body>

<svg class="abs scene" width="686" height="1200" viewBox="0 0 686 1200">
  <defs>
    <linearGradient id="skyline" x1="0" y1="0" x2="0" y2="1">
      <stop offset="0" stop-color="#e4e8ec"/>
      <stop offset=".22" stop-color="#c3c8cd"/>
      <stop offset=".42" stop-color="#70757b"/>
      <stop offset=".65" stop-color="#3b3e43"/>
      <stop offset="1" stop-color="#1e1f22"/>
    </linearGradient>
    <radialGradient id="heroGlow" cx=".5" cy=".35" r=".6">
      <stop offset="0" stop-color="#ffffff" stop-opacity=".12"/>
      <stop offset="1" stop-color="#000000" stop-opacity=".18"/>
    </radialGradient>
    <linearGradient id="bridgeTone" x1="0" y1="0" x2="1" y2="0">
      <stop offset="0" stop-color="#ffffff" stop-opacity="0"/>
      <stop offset=".45" stop-color="#d99c98" stop-opacity=".35"/>
      <stop offset=".8" stop-color="#b9585a" stop-opacity=".8"/>
      <stop offset="1" stop-color="#9c3a3e" stop-opacity=".9"/>
    </linearGradient>
    <linearGradient id="bridgeFadeTop" x1="0" y1="0" x2="0" y2="1">
      <stop offset="0" stop-color="#ffffff" stop-opacity="1"/>
      <stop offset=".12" stop-color="#ffffff" stop-opacity="0"/>
    </linearGradient>
    <linearGradient id="bay" x1="0" y1="0" x2="0" y2="1">
      <stop offset="0" stop-color="#ffffff" stop-opacity="0"/>
      <stop offset=".5" stop-color="#c6d0d2" stop-opacity=".55"/>
      <stop offset="1" stop-color="#8fa7ab" stop-opacity=".85"/>
    </linearGradient>
    <linearGradient id="cityDark" x1="0" y1="0" x2="0" y2="1">
      <stop offset="0" stop-color="#4a484b"/>
      <stop offset=".45" stop-color="#302f32"/>
      <stop offset="1" stop-color="#1f1e21"/>
    </linearGradient>
    <radialGradient id="cityGlow" cx=".55" cy=".4" r=".7">
      <stop offset="0" stop-color="#5a5659" stop-opacity=".35"/>
      <stop offset="1" stop-color="#000000" stop-opacity=".2"/>
    </radialGradient>
  </defs>

  <g role="img" aria-label="Photo of the Golden Gate Bridge over the bay">
    <rect x="0" y="620" width="686" height="130" fill="url(#bay)"/>
    <rect x="470" y="320" width="216" height="430" fill="url(#bridgeTone)"/>
    <rect x="470" y="320" width="216" height="430" fill="url(#bridgeFadeTop)"/>
  </g>

  <polygon points="0,296 464,381 686,287 686,0 0,0" fill="var(--red)"/>
  <g role="img" aria-label="Aerial photo of a city skyline">
    <polygon points="0,296 464,366 686,287 686,0 0,0" fill="url(#skyline)"/>
    <polygon points="0,296 464,366 686,287 686,0 0,0" fill="url(#heroGlow)"/>
  </g>

  <polygon points="0,751 221,657 686,737 686,1030 0,1030" fill="var(--red)"/>
  <g role="img" aria-label="Darkened aerial photo of downtown towers">
    <polygon points="0,765 221,671 686,750 686,1030 0,1030" fill="url(#cityDark)"/>
    <polygon points="0,765 221,671 686,750 686,1030 0,1030" fill="url(#cityGlow)"/>
  </g>
</svg>

<div class="abs topbar">
  <div class="abs social" aria-label="Social links">
    <span class="dot"></span><span class="dot"></span><span class="dot"></span><span class="dot"></span>
  </div>
  <div class="abs contact">
    <span>
      <svg width="8" height="8" viewBox="0 0 24 24"><path fill="#fff" d="M6.6 10.8a15 15 0 006.6 6.6l2.2-2.2c.3-.3.7-.4 1-.2 1.1.4 2.3.6 3.6.6.6 0 1 .4 1 1V20c0 .6-.4 1-1 1A17 17 0 013 4c0-.6.4-1 1-1h3.5c.6 0 1 .4 1 1 0 1.2.2 2.4.6 3.6.1.3 0 .7-.2 1z"/></svg>
      +987 555 0142
    </span>
    <span>
      <svg width="9" height="7" viewBox="0 0 24 18"><path fill="#fff" d="M0 0h24v3L12 10 0 3zM0 5l12 7 12-7v13H0z"/></svg>
      info@valmikegroup.com
    </span>
  </div>
</div>

<div class="abs brand header-brand">
  <span class="brand-mark"></span>
  <span class="brand-name">VALMIKE<br>GROUP</span>
</div>
<nav class="abs nav">
  <a class="active" style="left:0">Home</a>
  <a style="left:52px">About Us</a>
  <a style="left:120px">Services</a>
  <a style="left:183px">Iron Finch</a>
  <a style="left:246px">Contact Us</a>
</nav>

<h1 class="abs hero-title display">NEW ERA IN PROTECTION</h1>
<div class="abs cta">
  <span class="cta-square"></span>
  <span class="cta-label">CONTACT US</span>
</div>

<div class="abs services-eyebrow display">SERVICES</div>
<h2 class="abs services-title display">WHAT WE OFFER</h2>

<div class="abs service" style="left:102px;top:482px">
  <svg class="service-icon" viewBox="0 0 78 86" role="img" aria-label="Executive protection icon">
    <rect x="0" y="0" width="78" height="86" rx="4" fill="var(--frame)"/>
    <rect x="8" y="8" width="62" height="70" rx="2" fill="var(--frame-inner)"/>
    <circle cx="46" cy="35" r="6" fill="#2b2b2b"/>
    <path d="M35 54c0-7 5-11 11-11s11 4 11 11z" fill="#2b2b2b"/>
    <circle cx="31" cy="35" r="6" fill="#2b2b2b"/>
    <path d="M19 54c0-7 5-11 12-11s12 4 12 11z" fill="var(--red)"/>
  </svg>
  <div class="service-name">Executive<br>Protection</div>
</div>
<div class="abs service" style="left:273px;top:482px">
  <svg class="service-icon" viewBox="0 0 78 86" role="img" aria-label="Covert protection icon">
    <rect x="0" y="0" width="78" height="86" rx="4" fill="var(--frame)"/>
    <rect x="8" y="8" width="62" height="70" rx="2" fill="var(--frame-inner)"/>
    <circle cx="22" cy="35" r="5.5" fill="#2b2b2b"/>
    <path d="M12 54c0-6 4-10 10-10s10 4 10 10z" fill="#2b2b2b"/>
    <circle cx="56" cy="35" r="5.5" fill="#2b2b2b"/>
    <path d="M46 54c0-6 4-10 10-10s10 4 10 10z" fill="#2b2b2b"/>
    <circle cx="39" cy="35" r="6" fill="#2b2b2b"/>
    <path d="M28 54c0-7 5-11 11-11s11 4 11 11z" fill="var(--red)"/>
  </svg>
  <div class="service-name">Covert<br>Protection</div>
</div>
<div class="abs service" style="left:444px;top:482px">
  <svg class="service-icon" viewBox="0 0 78 86" role="img" aria-label="Residential protection icon">
    <rect x="0" y="0" width="78" height="86" rx="4" fill="var(--frame)"/>
    <rect x="8" y="8" width="62" height="70" rx="2" fill="var(--frame-inner)"/>
    <rect x="35" y="24" width="8" height="5" fill="#2b2b2b"/>
    <polygon points="39,27 22,40 56,40" fill="var(--red)"/>
    <rect x="23" y="41" width="32" height="15" fill="#2b2b2b"/>
    <rect x="27" y="45" width="6" height="7" fill="var(--frame-inner)"/>
    <rect x="36" y="45" width="6" height="7" fill="var(--frame-inner)"/>
    <rect x="45" y="45" width="6" height="7" fill="var(--frame-inner)"/>
  </svg>
  <div class="service-name">Residential Protection<br>&amp; Intelligence</div>
</div>

<div class="abs about-emblem"><span>VALMIKE</span></div>
<div class="abs about-eyebrow display">ABOUT</div>
<div class="abs about-title display"><span class="big">VALMIKE</span><span class="small">GROUP</span></div>
<p class="abs about-lead">Consectetuer adipiscing elit, sed diam nonummy nibh euismod tincidunt ut laoreet dolore magna aliquam erat volutpat.</p>
<p class="abs about-body">Suscipit lobortis nisl ut aliquip ex ea commodo consequat. Duis autem vel eum iriure dolor in hendrerit in vulputate velit esse molestie consequat, vel illum dolore eu feugiat nulla facilisis at vero eros et accumsan et iusto odio dignissim qui blandit praesent luptatum zzril delenit augue duis dolore te feugait nulla facilisi.</p>
<div class="abs read-more"><span class="sq"></span><span class="label">READ MORE</span></div>

<footer class="abs footer">
  <div class="abs brand footer-brand">
    <span class="brand-mark"></span>
    <span class="brand-name">VALMIKE<br>GROUP</span>
  </div>
  <div class="abs footer-contact" style="left:351px">
    <span class="footer-icon"><svg width="9" height="9" viewBox="0 0 24 24"><path fill="#fff" d="M6.6 10.8a15 15 0 006.6 6.6l2.2-2.2c.3-.3.7-.4 1-.2 1.1.4 2.3.6 3.6.6.6 0 1 .4 1 1V20c0 .6-.4 1-1 1A17 17 0 013 4c0-.6.4-1 1-1h3.5c.6 0 1 .4 1 1 0 1.2.2 2.4.6 3.6.1.3 0 .7-.2 1z"/></svg></span>
    +987 555 0142
  </div>
  <div class="abs footer-divider"></div>
  <div class="abs footer-contact" style="left:477px">
    <span class="footer-icon"><svg width="10" height="8" viewBox="0 0 24 18"><path fill="#fff" d="M0 0h24v3L12 10 0 3zM0 5l12 7 12-7v13H0z"/></svg></span>
    info@valmikegroup.com
  </div>
  <nav class="abs footer-nav">
    <span class="item" style="left:28px">Home</span>
    <span class="sep" style="left:57px"></span>
    <span class="item" style="left:92px">About Us</span>
    <span class="sep" style="left:128px"></span>
    <span class="item" style="left:161px">Services</span>
    <span class="sep" style="left:195px"></span>
    <span class="item" style="left:227px">Iron Finch</span>
    <span class="sep" style="left:261px"></span>
    <span class="item" style="left:300px">Contact Us</span>
    <span class="sep" style="left:339px"></span>
    <span class="item" style="left:358px;top:8px"><span class="dot"></span></span>
    <span class="sep" style="left:378px"></span>
    <span class="item" style="left:398px;top:8px"><span class="dot"></span></span>
    <span class="sep" style="left:419px"></span>
    <span class="item" style="left:439px;top:8px"><span class="dot"></span></span>
    <span class="sep" style="left:460px"></span>
    <span class="item" style="left:480px;top:8px"><span class="dot"></span></span>
  </nav>
</footer>
<div class="abs copyright">
  <span class="abs left">Copyright © 2021 Valmike Group. All Rights Reserved.</span>
  <span class="abs right">Privacy Policy</span>
</div>

</body>
</html>
```